Realtor Business Card for Marisol!

I sell real estate in a tropical location near the ocean, beaches and palm trees.

The homes are higher end, luxury. I want a card that is professional and attention-grabbing. In a sea full of competition, I need to stand out! I don't want the run-of-the mill card that looks like everyone else's with a different name. I want people to say "wow!".
Updates

Project Deadline Extended Reason: I have a little more time that originally anticipated. Added Friday, July 7, 2017

Target Market(s)

All.

Industry/Entity Type

Real Estate Agent

Contact Information for Business Card

Name: Marisol Vankeer-Odham
Email: marisol@harborview-estates.example
Website: www.harborviewestates.example
Phone: 555.418.7263

Font styles to use
Serif

Colors

Designer to choose colors to be used in the design.

Requirements
Must have
• All attachments.
Nice to have
• Gold edges
• Transparent card
• Unique shape

```html
<!DOCTYPE html>
<html lang="en">
<head>
<meta charset="utf-8">
<title>Marisol Vankeer-Odham — Business Card</title>
<link rel="stylesheet" href="https://fonts.googleapis.com/css2?family=Open+Sans:wght@400;700&display=swap">
<style>
  :root {
    --card-bg: #e8eeed;
    --brand-red: #bb2030;
    --ink-gray: #4d5152;
    --band-light: #e4eceb;
  }
  * { margin: 0; padding: 0; box-sizing: border-box; }
  html, body { width: 720px; height: 1200px; overflow: hidden; background: var(--card-bg); }
  .card {
    position: relative;
    width: 720px;
    height: 1200px;
    background: var(--card-bg);
    font-family: "Open Sans", Arial, sans-serif;
    overflow: hidden;
  }
  .portrait {
    position: absolute;
    left: 0;
    top: 0;
    width: 720px;
    height: 600px;
  }
  .agent-name {
    position: absolute;
    left: 0;
    width: 720px;
    top: 600px;
    text-align: center;
    font-weight: 700;
    font-size: 54px;
    letter-spacing: 0.2px;
    white-space: nowrap;
    color: var(--brand-red);
  }
  .agent-name .surname-tail { color: var(--ink-gray); }
  .contact-list { list-style: none; }
  .contact-item {
    position: absolute;
    left: 82px;
    display: flex;
    align-items: center;
    color: var(--ink-gray);
    white-space: nowrap;
  }
  .contact-item svg { width: 24px; height: 24px; margin-right: 36px; flex: none; }
  .contact-phone { top: 740px; font-size: 36px; }
  .contact-email { top: 852px; font-size: 28px; }
  .contact-web { top: 956px; font-size: 31px; }
  .footer-band {
    position: absolute;
    left: 0;
    top: 1064px;
    width: 720px;
    height: 74px;
    background: var(--brand-red);
  }
  .footer-strip {
    position: absolute;
    left: 0;
    top: 1142px;
    width: 720px;
    height: 58px;
    background: var(--band-light);
  }
</style>
</head>
<body>
<div class="card">
  <svg class="portrait" viewBox="0 0 720 600" xmlns="http://www.w3.org/2000/svg">
    <defs>
      <linearGradient id="portraitTones" x1="0" y1="0" x2="1" y2="1">
        <stop offset="0" stop-color="#8a8f8c"/>
        <stop offset="0.35" stop-color="#d9a98c"/>
        <stop offset="0.6" stop-color="#c9b7a7"/>
        <stop offset="0.85" stop-color="#b5505a"/>
        <stop offset="1" stop-color="#3c3f44"/>
      </linearGradient>
    </defs>
    <path class="accent-blob" fill="var(--brand-red)"
      d="M 110 250 C 130 150, 240 90, 340 78 C 420 70, 470 120, 500 200 C 540 300, 520 450, 470 555 C 440 585, 360 575, 300 548 C 200 512, 90 420, 85 330 C 82 300, 95 270, 110 250 Z"/>
    <path class="photo-frame" fill="url(#portraitTones)" role="img"
      aria-label="Portrait photo of the agent in a modern living room"
      d="M 100 300 C 110 170, 170 100, 260 95 L 420 92 C 520 97, 600 230, 630 360 C 640 410, 600 440, 540 470 C 460 510, 380 540, 300 540 L 150 540 C 110 540, 100 510, 100 470 Z"/>
  </svg>

  <h1 class="agent-name">Marisol Vankeer<span class="surname-tail">-Odham</span></h1>

  <ul class="contact-list">
    <li class="contact-item contact-phone">
      <svg viewBox="0 0 24 24"><path fill="var(--brand-red)" d="M8 3c1.5 0 2.5 1 2.5 2s-1.5 1.5-1.5 2.5 0 5 0 6 1.5 1.5 1.5 2.5-1 2-2.5 2l-1-1c.8-.5 1-1 .5-1.5-.8-.8-1-3.5-1-5s.2-4.2 1-5c.5-.5.3-1-.5-1.5z"/></svg>
      <span>555.418.7263</span>
    </li>
    <li class="contact-item contact-email">
      <svg viewBox="0 0 24 24" fill="none" stroke="var(--brand-red)" stroke-width="1.6"><rect x="2" y="5" width="20" height="14"/><path d="M2 5l10 8 10-8M2 19l7-7M22 19l-7-7"/></svg>
      <span>marisol@harborview-estates.example</span>
    </li>
    <li class="contact-item contact-web">
      <svg viewBox="0 0 24 24" fill="none" stroke="var(--brand-red)" stroke-width="1.6"><circle cx="12" cy="12" r="10"/><ellipse cx="12" cy="12" rx="4.5" ry="10"/><path d="M2 12h20M4 7h16M4 17h16"/></svg>
      <span>www.harborviewestates.example</span>
    </li>
  </ul>

  <div class="footer-band"></div>
  <div class="footer-strip"></div>
</div>
</body>
</html>
```